Banner Ad Design Project -Oil and Gas Value Chain

I am needing to create a simple graphic like the one here:

size: 720x300
http://plumwickstudio.example/designresources/banners/examples/720x300.php

Oil and Gas Value Chain:
The oil industry has three levels: upstream, midstream, and downstream which encompass the main segments in the supply chain. The upstream level includes the exploration, drilling, and production of crude oil and the midstream level includes the transportation and trading of crude oil to refineries. The downstream level refers to the refining of crude oil into finished product, the storage of crude oil, and the distribution and marketing of crude oil to wholesalers and retailers.

http://www.quarnelbriefs.example/images/value_chain.gif
http://www.tarvoskilearn.example/modules/m008/imgs/fig_001.jpg
Here is another that is more for reference:

http://www.hollin.example/web/soc142/team9/GVC_clip_image002.jpg

https://www.zembrafind.example/search?q=oil+value+chain&hl=en&tbo=u&prmd=imvns&tbm=isch&source=univ&sa=X&ei=I1hsUOuEC-SK2wXry4DAAg&ved=0CDMQsAQ&biw=1680&bih=925

```html
<!DOCTYPE html>
<html lang="en">
<head>
<meta charset="utf-8">
<title>Oil and Gas Value Chain</title>
<link rel="stylesheet" href="https://fonts.googleapis.com/css2?family=Roboto+Condensed:wght@300;400&display=swap">
<style>
  :root {
    --paper: #ffffff;
    --ink: #111111;
    --art-fill: #e6e6e6;
    --art-edge: #c4c4c4;
  }
  html, body {
    margin: 0;
    padding: 0;
    overflow: hidden;
    background: var(--paper);
  }
  .banner {
    position: relative;
    width: 1200px;
    height: 504px;
    background: var(--paper);
    color: var(--ink);
    font-family: "Roboto Condensed", "Arial Narrow", sans-serif;
    font-weight: 400;
    overflow: hidden;
  }
  .banner__frame {
    position: absolute;
    inset: 0;
    width: 1200px;
    height: 504px;
  }
  .frame-line {
    fill: none;
    stroke: var(--ink);
    stroke-width: 1.6;
    vector-effect: non-scaling-stroke;
  }
  .art {
    fill: var(--art-fill);
    stroke: var(--art-edge);
    stroke-width: 1;
    vector-effect: non-scaling-stroke;
  }
  .label {
    position: absolute;
    margin: 0;
    line-height: 1;
    white-space: nowrap;
    letter-spacing: -0.01em;
  }
  .label--explore { left: 136px; top: 90px; font-size: 72px; }
  .label--drill { left: 196px; top: 286px; font-size: 50px; }
  .label--drill-amp { left: 310px; top: 286px; font-size: 50px; }
  .label--produce { left: 196px; top: 344px; font-size: 50px; }
  .label--transport { left: 484px; top: 140px; font-size: 42px; }
  .label--transport-amp { left: 540px; top: 178px; font-size: 42px; }
  .label--trade { left: 500px; top: 214px; font-size: 42px; }
  .label--dollar { left: 558px; top: 322px; font-size: 46px; }
  .label--refine { left: 950px; top: 32px; font-size: 44px; }
  .label--refine-amp { left: 980px; top: 78px; font-size: 44px; }
  .label--store { left: 946px; top: 122px; font-size: 44px; }
  .label--distribute { left: 804px; top: 228px; font-size: 42px; }
  .stage {
    position: absolute;
    top: 432px;
    margin: 0;
    font-size: 42px;
    line-height: 1;
    font-weight: 300;
  }
  .stage--upstream { left: 64px; }
  .stage--midstream { left: 492px; }
  .stage--downstream { left: 900px; }
</style>
</head>
<body>
<main class="banner">
  <svg class="banner__frame" viewBox="0 0 722 302" preserveAspectRatio="none">
    <rect class="art" role="img" aria-label="Line drawing of an oil derrick" x="20" y="5" width="42" height="106"/>
    <rect class="art" role="img" aria-label="Line drawing of a pumpjack at a well" x="6" y="112" width="104" height="132"/>
    <rect class="art" role="img" aria-label="Line drawing of a tanker truck" x="255" y="10" width="190" height="68"/>
    <rect class="art" role="img" aria-label="Line drawing of two traders shaking hands" x="285" y="166" width="125" height="80"/>
    <rect class="art" role="img" aria-label="Line drawing of refinery equipment" x="486" y="8" width="68" height="100"/>
    <rect class="art" role="img" aria-label="Line drawing of an oil barrel" x="662" y="38" width="44" height="74"/>
    <rect class="art" role="img" aria-label="Line drawing of a fuel station canopy with pumps" x="515" y="178" width="200" height="68"/>

    <rect class="frame-line" x="1" y="1" width="720" height="300"/>
    <line class="frame-line" x1="1" y1="250" x2="721" y2="250"/>
    <path class="frame-line" d="M222,1 L222,38 C272,32 272,118 222,112 L222,250"/>
    <path class="frame-line" d="M476,1 L476,52 C424,46 424,132 476,126 L478,250"/>
  </svg>

  <p class="label label--explore">Explore</p>
  <p class="label label--drill">Drill</p>
  <p class="label label--drill-amp">&amp;</p>
  <p class="label label--produce">Produce</p>

  <p class="label label--transport">Transport</p>
  <p class="label label--transport-amp">&amp;</p>
  <p class="label label--trade">Trade</p>
  <p class="label label--dollar">$</p>

  <p class="label label--refine">Refine</p>
  <p class="label label--refine-amp">&amp;</p>
  <p class="label label--store">Store</p>
  <p class="label label--distribute">Distribute</p>

  <p class="stage stage--upstream">Upstream</p>
  <p class="stage stage--midstream">Midstream</p>
  <p class="stage stage--downstream">Downstream</p>
</main>
</body>
</html>
```